Business card for STEADYWAVE

Please design professional business card for IT consulting firm STEADYWAVE INC.
Use logo attached.
Use information from sample qNode business card attached.
replace qnode inc with STEADYWAVE INC.
as well as qnodeinc.com with steadywave.example

```html
<!DOCTYPE html>
<html lang="en">
<head>
<meta charset="utf-8">
<title>STEADYWAVE Business Card</title>
<link rel="stylesheet" href="https://fonts.googleapis.com/css2?family=Montserrat:wght@400;500;700;800&display=swap">
<style>
  :root {
    --stage: #2a2a2c;
    --card: #111112;
    --card-edge: #1c1c1e;
    --white: #ffffff;
    --soft-white: #e6e6e6;
    --teal: #5fd0ad;
    --sky: #3cb4ea;
    --violet: #7a3fb0;
    --amber: #f39a1e;
    --pattern-dark: #1a1a1b;
    --pattern-light: #3b3b3d;
  }
  * { margin: 0; padding: 0; box-sizing: border-box; }
  html, body { width: 1200px; height: 900px; overflow: hidden; }
  body {
    background: var(--stage);
    font-family: "Montserrat", sans-serif;
    color: var(--white);
    display: flex;
    flex-direction: column;
    align-items: center;
    justify-content: center;
    gap: 56px;
  }
  .card {
    position: relative;
    width: 620px;
    height: 354px;
    border-radius: 22px;
    background: var(--card);
    overflow: hidden;
    box-shadow: 0 18px 40px rgba(0,0,0,.45);
  }

  /* ---------- front ---------- */
  .wordmark {
    font-weight: 800;
    letter-spacing: 0.14em;
    text-transform: uppercase;
    color: var(--white);
    display: flex;
    align-items: center;
    gap: 10px;
    line-height: 1;
  }
  .wordmark-square {
    display: inline-block;
    background: var(--teal);
  }
  .front .wordmark {
    position: absolute;
    top: 46px;
    right: 44px;
    font-size: 38px;
  }
  .front .wordmark-square { width: 20px; height: 20px; }

  .name-row {
    position: absolute;
    top: 122px;
    left: 0;
    right: 36px;
    display: flex;
    align-items: center;
    gap: 14px;
  }
  .rule { height: 1.5px; background: var(--teal); }
  .rule-lead { width: 150px; }
  .rule-tail { flex: 1; }
  .person-name {
    font-weight: 700;
    font-size: 19px;
    letter-spacing: 0.04em;
    color: var(--teal);
    text-transform: uppercase;
    white-space: nowrap;
  }
  .person-name small { font-size: 14px; }
  .job-title {
    position: absolute;
    top: 152px;
    left: 164px;
    font-size: 14px;
    font-weight: 500;
    color: var(--soft-white);
  }

  .contact-list {
    position: absolute;
    left: 36px;
    top: 200px;
    list-style: none;
    font-size: 13.5px;
    line-height: 1.75;
    color: var(--soft-white);
  }
  .contact-list li { display: flex; align-items: center; gap: 10px; }
  .contact-list svg { width: 13px; height: 13px; flex: none; fill: var(--sky); }

  .company-address {
    position: absolute;
    right: 40px;
    top: 214px;
    text-align: right;
    font-size: 14px;
    line-height: 1.55;
    color: var(--soft-white);
    font-style: normal;
  }
  .company-address .company-name { color: var(--sky); font-weight: 500; }

  .spectrum-edge {
    position: absolute;
    left: 0; right: 0; bottom: 0;
    height: 7px;
    background: linear-gradient(90deg, var(--violet), var(--teal) 40%, var(--sky) 65%, var(--amber));
  }

  /* ---------- back ---------- */
  .back-pattern {
    position: absolute;
    inset: 0;
    background: linear-gradient(135deg, var(--pattern-dark) 0%, var(--pattern-light) 55%, var(--pattern-dark) 100%);
  }
  .back .wordmark {
    position: absolute;
    top: 50%;
    left: 50%;
    transform: translate(-50%, -50%);
    font-size: 44px;
  }
  .back .wordmark-square { width: 22px; height: 22px; }
</style>
</head>
<body>

  <section class="card front" aria-label="Card front">
    <div class="wordmark">STEADYWAVE<span class="wordmark-square"></span></div>

    <div class="name-row">
      <span class="rule rule-lead"></span>
      <h1 class="person-name">Dorian Velasko, <small>P. Eng.</small></h1>
      <span class="rule rule-tail"></span>
    </div>
    <p class="job-title">General Manager</p>

    <ul class="contact-list">
      <li>
        <svg viewBox="0 0 24 24" aria-hidden="true"><path d="M6.6 10.8a15 15 0 0 0 6.6 6.6l2.2-2.2a1 1 0 0 1 1-.25 11.4 11.4 0 0 0 3.6.57 1 1 0 0 1 1 1V20a1 1 0 0 1-1 1A17 17 0 0 1 3 4a1 1 0 0 1 1-1h3.5a1 1 0 0 1 1 1c0 1.25.2 2.45.57 3.57a1 1 0 0 1-.25 1z"/></svg>
        (555) 014-2270 ext.201
      </li>
      <li>
        <svg viewBox="0 0 24 24" aria-hidden="true"><path d="M7 1h10a2 2 0 0 1 2 2v18a2 2 0 0 1-2 2H7a2 2 0 0 1-2-2V3a2 2 0 0 1 2-2zm0 3v15h10V4zm5 16.2a1 1 0 1 0 0 .01z"/></svg>
        (555) 019-3381
      </li>
      <li>
        <svg viewBox="0 0 24 24" aria-hidden="true"><path d="M2 5h20v14H2zm2 2v.5l8 5 8-5V7zm0 2.8V17h16V9.8l-8 5z"/></svg>
        dvelasko@steadywave.example
      </li>
      <li>
        <svg viewBox="0 0 24 24" aria-hidden="true"><path d="M12 2a10 10 0 1 0 0 20 10 10 0 0 0 0-20zm0 2c1 0 2.3 2 2.8 5H9.2C9.7 6 11 4 12 4zm-8 8c0-.7.1-1.4.3-2h3c-.1.7-.1 1.3-.1 2s0 1.3.1 2h-3A8 8 0 0 1 4 12zm5.2 3h5.6c-.5 3-1.8 5-2.8 5s-2.3-2-2.8-5zm7.5-1c.1-.7.1-1.3.1-2s0-1.3-.1-2h3a8 8 0 0 1 0 4z"/></svg>
        www.steadywave.example
      </li>
    </ul>

    <address class="company-address">
      <span class="company-name">STEADYWAVE INC.</span><br>
      1280 Harbor Crest RD., Suite 101<br>
      Lakeview, Ontario<br>
      K0A 1B2, Canada
    </address>

    <div class="spectrum-edge"></div>
  </section>

  <section class="card back" aria-label="Card back">
    <div class="back-pattern" role="img" aria-label="Repeating pattern of dark and grey plus signs"></div>
    <div class="wordmark">STEADYWAVE<span class="wordmark-square"></span></div>
  </section>

</body>
</html>
```